Business Card Design Project

We need a logo design for a new company based in Southern California called "Brocklin Security Services, Inc." We install security and camera systems for homeowners and business, to protect their assets.
Updates

Project Deadline Extended
Reason: LOGO Design completes in eight days. Would like that design decided before we finish the business cards. Thanks...

Target Market(s)

Homeowners and business owners looking for additional protection of their assets.

Industry/Entity Type

Security

Font styles to use
Serif

Requirements
Must have
• Company Name
Office# 555-204-6137
Service# 555-204-6138
email: BrocklinSecurity@quorvex.net
address: 48210 Maple Row Harlow Springs, CA 90000
Nice to have
• Serving Southern California

```html
<!DOCTYPE html>
<html lang="en">
<head>
<meta charset="utf-8">
<title>Brocklin Security Services, Inc. – Business Card</title>
<link rel="stylesheet" href="https://fonts.googleapis.com/css2?family=Cinzel:wght@400&family=Crimson+Text:wght@400&display=swap">
<style>
  :root {
    --backdrop: #2b2b2b;
    --card-aqua: #a9d8dc;
    --card-aqua-light: #b9e1e4;
    --card-aqua-deep: #98cdd2;
    --gold: #8a6a1c;
    --mark-white: #ffffff;
  }
  * { margin: 0; padding: 0; box-sizing: border-box; }
  html, body {
    width: 1200px;
    height: 869px;
    overflow: hidden;
    background: var(--backdrop);
  }
  .card {
    position: absolute;
    left: 150px;
    top: 177px;
    width: 900px;
    height: 514px;
    background: var(--card-aqua);
    overflow: hidden;
  }
  .card-pattern {
    position: absolute;
    inset: 0;
    background:
      radial-gradient(circle at 30% 40%, var(--card-aqua-light) 0%, transparent 55%),
      radial-gradient(circle at 75% 65%, var(--card-aqua-deep) 0%, transparent 60%),
      var(--card-aqua);
  }
  .brand {
    position: absolute;
    left: 58px;
    top: 82px;
    display: flex;
    align-items: center;
    gap: 28px;
  }
  .brand-circle { display: block; }
  .brand-name {
    font-family: "Cinzel", serif;
    font-weight: 400;
    font-size: 31px;
    letter-spacing: 1.5px;
    color: var(--gold);
  }
  .contact {
    position: absolute;
    left: 62px;
    top: 270px;
    list-style: none;
    font-family: "Crimson Text", serif;
    font-size: 19px;
    line-height: 37px;
    color: var(--gold);
  }
  .tagline {
    position: absolute;
    left: 62px;
    top: 462px;
    font-family: "Crimson Text", serif;
    font-size: 19px;
    line-height: 24px;
    color: var(--gold);
  }
</style>
</head>
<body>
  <div class="card">
    <div class="card-pattern" role="img" aria-label="Faint tone-on-tone damask pattern across the aqua card"></div>

    <div class="brand">
      <svg class="brand-circle" width="110" height="110" viewBox="0 0 110 110" aria-hidden="true">
        <circle cx="55" cy="55" r="51" fill="none" stroke="var(--mark-white)" stroke-width="4"/>
      </svg>
      <h1 class="brand-name">Brocklin Security Services, Inc.</h1>
    </div>

    <ul class="contact">
      <li>Office number: 555-204-6137</li>
      <li>Service number: 555-204-6138</li>
      <li>E-mail: BrocklinSecurity@quorvex.net</li>
      <li>Address: 48210 Maple Row Harlow Springs, CA 90000</li>
    </ul>

    <p class="tagline">Serving Southern California</p>
  </div>
</body>
</html>
```